Sleek, Professional Business Card Design Needed

Business Cards - Logo Attached.

We are a solar consulting company. We are national and want our cards to represent the professional high quality products that we offer.

Industry/Entity Type

Business

Contact Information for Business Card

n/a

Requirements
Must have
• Design
• Name
• Position
• Number
• Email
• Address
Should not have
• Not be too crowded

```html
<!DOCTYPE html>
<html lang="en">
<head>
<meta charset="utf-8">
<title>Bright Field Energy – Business Card</title>
<link href="https://fonts.googleapis.com/css2?family=Lato:wght@400;700&display=swap" rel="stylesheet">
<style>
  :root {
    --page-bg: #e9eef1;
    --card-bg: #f4f7f3;
    --ink: #3c4446;
    --brand-blue: #1f8fc4;
    --brand-green: #6fae2e;
    --band-green: #6a9f2a;
    --band-teal: #10786a;
    --ring: rgba(60, 90, 80, 0.08);
  }
  html, body {
    margin: 0;
    width: 1200px;
    height: 927px;
    overflow: hidden;
    background: var(--page-bg);
    font-family: "Lato", sans-serif;
  }
  .card {
    position: absolute;
    left: 110px;
    top: 183px;
    width: 980px;
    height: 560px;
    background: var(--card-bg);
    box-shadow: 0 18px 40px rgba(0, 0, 0, 0.12);
    overflow: hidden;
  }
  .brand {
    position: absolute;
    left: 70px;
    top: 62px;
    display: flex;
    align-items: center;
    gap: 18px;
  }
  .brand-dot {
    width: 70px;
    height: 70px;
    border-radius: 50%;
    border: 7px solid var(--brand-blue);
    box-sizing: border-box;
  }
  .brand-name {
    font-weight: 700;
    font-size: 38px;
    color: var(--brand-blue);
    letter-spacing: 0.5px;
  }
  .decor-ring {
    position: absolute;
    right: 70px;
    top: 60px;
    width: 340px;
    height: 340px;
    border-radius: 50%;
    border: 22px solid var(--ring);
    box-sizing: border-box;
  }
  .person {
    position: absolute;
    left: 70px;
    top: 300px;
    color: var(--ink);
  }
  .person-name {
    font-weight: 700;
    font-size: 40px;
    margin: 0;
  }
  .person-role {
    font-size: 24px;
    color: var(--brand-green);
    margin: 4px 0 22px;
  }
  .contact-line {
    font-size: 24px;
    margin: 4px 0;
  }
  .contact-line b {
    color: var(--band-teal);
    font-weight: 700;
  }
  .address {
    position: absolute;
    right: 70px;
    top: 370px;
    text-align: right;
    font-size: 26px;
    line-height: 1.3;
    color: var(--ink);
  }
  .band {
    position: absolute;
    left: 0;
    bottom: 0;
    width: 980px;
    height: 70px;
  }
  .web {
    position: absolute;
    right: 70px;
    bottom: 14px;
    font-size: 26px;
    font-weight: 700;
    color: #ffffff;
  }
</style>
</head>
<body>
  <div class="card">
    <div class="brand">
      <div class="brand-dot"></div>
      <div class="brand-name">BRIGHT FIELD ENERGY</div>
    </div>

    <div class="decor-ring"></div>

    <div class="person">
      <p class="person-name">Dana Reyes</p>
      <p class="person-role">Vice President</p>
      <p class="contact-line"><b>T :</b> 001 555 0199</p>
      <p class="contact-line"><b>E :</b> info@brightfieldenergy.com</p>
    </div>

    <div class="address">
      18 Harbor Rd, Suite 4<br>
      Lakeview, Country 40517
    </div>

    <svg class="band" viewBox="0 0 980 70" preserveAspectRatio="none">
      <rect x="0" y="44" width="600" height="26" fill="var(--band-green)"/>
      <polygon points="540,0 980,0 980,70 510,70" fill="var(--band-teal)"/>
    </svg>
    <div class="web">www.brightfieldenergy.com</div>
  </div>
</body>
</html>
```